Home Improvements Website

I would like a website that matches our business colour scheme and uses the fonts consistent without logo. (Monserrat, Chosence & Big Noddle Tiling).
We will need numerous sections: homepage, about us, services (with tiles or links to each service - building, landscaping, decking, maintenance, roofing, gutters etc) current projects (which must be easily editable by me, who is not too tech savvy) and a contacts page with enquiry form we can link to our job management service (Tradify).

```html
<!DOCTYPE html>
<html lang="en">
<head>
<meta charset="utf-8">
<title>Calloway Building &amp; Landscaping</title>
<link href="https://fonts.googleapis.com/css2?family=Bebas+Neue&family=Montserrat:wght@400;500;600;700&display=swap" rel="stylesheet">
<style>
:root{
  --gold:#a68a47;
  --gold-dark:#8d7439;
  --lime:#a3c83c;
  --green:#1f9a3c;
  --ink:#2b2b2b;
  --muted:#5e5e5e;
  --paper:#ffffff;
  --stone:#f3f1ee;
  --panel:#ecebe8;
  --field:#dedcd8;
  --navy:#243660;
  --footer:#353b3b;
}
*{box-sizing:border-box;margin:0;padding:0}
html,body{width:1200px;height:4854px;overflow:hidden}
body{position:relative;background:var(--paper);font-family:'Montserrat',sans-serif;color:var(--ink)}
.abs{position:absolute}
.display{font-family:'Bebas Neue',sans-serif;font-weight:400;letter-spacing:.5px;line-height:1}
.eyebrow{font-family:'Bebas Neue',sans-serif;color:var(--lime);font-size:17px;display:flex;align-items:center;gap:8px}
.eyebrow::before{content:"";width:26px;height:2px;background:var(--lime)}
.eyebrow.center{justify-content:center}
.btn{position:absolute;display:flex;align-items:center;justify-content:center;background:var(--gold);color:#fff;font-size:12.5px;font-weight:700;border-radius:12px;letter-spacing:.3px;box-shadow:0 4px 10px rgba(0,0,0,.12)}
.btn.ghost{background:transparent;border:2px solid #fff;box-shadow:none}
.photo{position:absolute;overflow:hidden}
.house{clip-path:polygon(50% 0,100% 24%,100% 100%,0 100%,0 24%)}
.roof{position:absolute;overflow:visible}
.brand{display:flex;align-items:center;gap:10px;font-family:'Montserrat',sans-serif;font-weight:700;font-size:20px;color:#fff;letter-spacing:1px}
.brand i{width:14px;height:14px;border-radius:50%;background:var(--lime);display:block}

/* hero */
.hero{left:0;top:0;width:1200px;height:675px;background:linear-gradient(100deg,#1e2d55 0%,#2c416f 40%,#6b7894 70%,#9aa3b3 100%);border-bottom-right-radius:90px;overflow:hidden}
.hero-shade{left:0;top:0;width:1200px;height:675px;background:linear-gradient(90deg,rgba(20,30,60,.7),rgba(20,30,60,0) 70%)}
.nav a{position:absolute;top:52px;color:#fff;font-size:12.5px;font-weight:600;text-decoration:none;letter-spacing:.3px}
.hero h1{left:113px;top:183px;font-size:64px;color:#fff;line-height:1.04}
.hero h2{left:113px;top:333px;font-size:29px;color:#fff;display:flex;gap:10px;align-items:center}
.hero h2 span{background:var(--green);padding:2px 6px;color:var(--lime)}
.hero p{left:113px;top:376px;width:520px;color:#fff;font-size:12.5px;line-height:1.55}

/* about */
.about{left:0;top:675px;width:1200px;height:681px;background:linear-gradient(90deg,#f4f4f6,#eef0f3)}
.about h2{font-size:46px;color:var(--ink)}
.about h3{font-size:25px}
.about p{font-size:12.5px;line-height:1.6;color:var(--muted)}

/* services */
.svc-panel{left:66px;top:1752px;width:1134px;height:354px;background:var(--stone);border-radius:30px 0 0 30px}
.svc-card .label{position:absolute;bottom:-52px;left:12px;right:12px;height:56px;background:var(--gold);color:#fff;border-radius:0 0 10px 10px;font-family:'Bebas Neue',sans-serif;font-size:28px;display:flex;align-items:center;justify-content:center}
.arrow-btn{position:absolute;width:44px;height:44px;border-radius:50%;display:flex;align-items:center;justify-content:center}

/* testimonials */
.testi{left:0;top:2990px;width:1200px;height:812px;background:var(--stone)}
.quote-card{position:absolute;background:#fff;border-radius:20px;text-align:center;box-shadow:0 6px 20px rgba(0,0,0,.05)}
.quote-card h4{font-family:'Bebas Neue',sans-serif;font-size:19px;font-weight:400}
.quote-card p{font-size:11.5px;line-height:1.6;color:var(--muted)}

/* contact */
.field{position:absolute;background:#fff;border-radius:8px;font-size:12px;color:#9a9a9a;padding:0 12px;display:flex;align-items:center}

/* footer */
.footer{left:0;top:4352px;width:1200px;height:502px;background:var(--footer);border-top-right-radius:60px}
.footer h5{position:absolute;font-family:'Bebas Neue',sans-serif;font-weight:400;font-size:17px;color:#fff;letter-spacing:.5px}
.footer .links a{position:absolute;display:block;font-size:11.5px;color:#b9bcbc;text-decoration:none}
.footer p,.footer .line{position:absolute;font-size:11.5px;color:#b9bcbc;line-height:1.65}
.footer .line{display:flex;gap:10px;align-items:center}
</style>
</head>
<body>

<!-- HERO -->
<section class="hero abs">
  <div class="photo" role="img" aria-label="Modern two-storey white house at dusk with lit interior and palm trees" style="left:0;top:0;width:1200px;height:675px;background:linear-gradient(100deg,#1b2a52 0%,#314a7a 45%,#8a93a8 75%,#c9c8c4 100%)"></div>
  <div class="abs hero-shade"></div>
  <div class="abs brand" style="left:122px;top:44px"><i></i>CALLOWAY</div>
  <nav class="nav">
    <a style="left:382px">HOME</a>
    <a style="left:463px">ABOUT US</a>
    <a style="left:573px">SERVICES &#8964;</a>
    <a style="left:693px">PROJECTS</a>
    <a style="left:804px">TESTIMONIALS</a>
  </nav>
  <div class="btn" style="left:946px;top:38px;width:143px;height:47px">CONTACT US</div>
  <h1 class="abs display">TRANSFORMING SPACES<br>WITH EXCELLENCE</h1>
  <h2 class="abs display">SPECIALIZING IN BUILDING, LANDSCAPING, DECKING, AND <span>MORE</span></h2>
  <p class="abs">At Calloway, we bring your vision to life with precision and care. From new constructions to beautiful landscapes and everything in between, our team is dedicated to delivering exceptional results</p>
  <div class="btn" style="left:113px;top:477px;width:226px;height:45px">EXPLORE OUR SERVICES</div>
  <div class="btn ghost" style="left:352px;top:477px;width:185px;height:45px">REQUEST A QUOTE</div>
  <div class="abs" style="left:1017px;top:573px;color:#fff;font-size:12.5px;font-weight:600">AUTO PLAY</div>
  <svg class="abs" style="left:1015px;top:625px" width="80" height="80" viewBox="0 0 80 80"><circle cx="40" cy="40" r="34" fill="#fff" stroke="var(--gold)" stroke-width="4"/><path d="M33 27 L53 40 L33 53 Z" fill="var(--gold)"/></svg>
</section>

<!-- ABOUT -->
<section class="about abs">
  <div class="abs" role="img" aria-label="Faint photo of a smiling construction worker" style="left:620px;top:0;width:580px;height:681px;background:radial-gradient(ellipse at 70% 40%,rgba(190,200,210,.35),rgba(238,240,243,0) 70%)"></div>
  <svg class="roof" style="left:180px;top:67px" width="350" height="110" viewBox="0 0 350 110"><polyline points="5,105 175,15 345,105" fill="none" stroke="var(--lime)" stroke-width="14"/><polyline points="30,115 175,38 320,115" fill="none" stroke="var(--navy)" stroke-width="6"/></svg>
  <div class="photo" role="img" aria-label="Modern house with large windows and landscaped garden" style="left:162px;top:110px;width:380px;height:470px;clip-path:polygon(50% 0,100% 22%,100% 80%,50% 100%,0 80%,0 22%);background:linear-gradient(180deg,#8ea3bd 0%,#3e4a55 45%,#4c6a3e 75%,#2e3b2a 100%)"></div>
  <svg class="roof" style="left:270px;top:530px" width="180" height="50" viewBox="0 0 180 50"><polyline points="5,5 90,40 175,5" fill="none" stroke="var(--green)" stroke-width="6"/></svg>
  <div class="photo" role="img" aria-label="Team of construction workers in hard hats" style="left:410px;top:240px;width:175px;height:175px;border-radius:40%;border:5px solid #fff;background:linear-gradient(135deg,#cfd8e3,#e6b94a 50%,#4e6fa1)"></div>
  <div class="photo" role="img" aria-label="Builder and homeowners reviewing plans" style="left:105px;top:335px;width:200px;height:210px;border-radius:42%;border:5px solid #fff;background:linear-gradient(135deg,#e0c889,#c9a064 50%,#6d7b8c)"></div>
  <div class="abs eyebrow" style="left:608px;top:191px">ABOUT US</div>
  <h2 class="abs display" style="left:608px;top:222px">WHO WE ARE</h2>
  <h3 class="abs display" style="left:608px;top:287px">DEDICATED TO QUALITY AND EXCELLENCE</h3>
  <p class="abs" style="left:608px;top:329px;width:480px">With years of experience in the industry, [Company Name] has established a reputation for delivering top-notch craftsmanship and outstanding customer service. Our team is passionate about creating spaces that reflect our clients' dreams and needs.</p>
  <div class="btn" style="left:603px;top:452px;width:226px;height:47px">LEARN MORE ABOUT US</div>
</section>

<!-- SERVICES -->
<section>
  <div class="abs eyebrow" style="left:117px;top:1416px">SERVICES</div>
  <h2 class="abs display" style="left:115px;top:1446px;font-size:46px">OUR SERVICES</h2>
  <h3 class="abs display" style="left:117px;top:1510px;font-size:25px">COMPREHENSIVE SOLUTIONS FOR ALL YOUR NEEDS</h3>
  <p class="abs" style="left:718px;top:1452px;width:380px;font-size:12.5px;line-height:1.6;color:var(--muted)">Explore our wide range of services designed to meet every requirement, from structural building to detailed landscaping. We handle it all with the utmost professionalism and care.</p>
  <div class="abs svc-panel"></div>

  <div class="abs svc-card" style="left:113px;top:1583px;width:284px;height:330px">
    <svg class="roof" style="left:-6px;top:-4px" width="296" height="80" viewBox="0 0 296 80"><polyline points="4,76 148,6 292,76" fill="none" stroke="var(--lime)" stroke-width="10"/></svg>
    <div class="photo house" role="img" aria-label="Brick commercial apartment building" style="left:0;top:10px;width:284px;height:320px;border-radius:0 0 14px 14px;background:linear-gradient(180deg,#b3c2d2,#7a3d2e 40%,#3c2a25)"></div>
    <p class="abs" style="left:40px;top:220px;width:204px;text-align:center;color:#fff;font-size:12.5px;line-height:1.55">Residential and commercial construction with a focus on durability and design</p>
    <div class="abs" style="left:127px;top:286px;width:30px;height:30px;border-radius:50%;background:rgba(255,255,255,.25);color:#fff;display:flex;align-items:center;justify-content:center;font-size:16px">&#8594;</div>
    <div class="label">BUILDING</div>
  </div>
  <div class="abs svc-card" style="left:427px;top:1583px;width:284px;height:330px">
    <svg class="roof" style="left:-6px;top:-4px" width="296" height="80" viewBox="0 0 296 80"><polyline points="4,76 148,6 292,76" fill="none" stroke="var(--lime)" stroke-width="10"/></svg>
    <div class="photo house" role="img" aria-label="White patio chairs on wooden decking beside a lawn" style="left:0;top:10px;width:284px;height:320px;border-radius:0 0 14px 14px;background:linear-gradient(180deg,#e8ecee 0%,#c9c2b4 45%,#a57d55 62%,#5aa33a 75%,#3f7d27)"></div>
    <div class="label">LANDSCAPING</div>
  </div>
  <div class="abs svc-card" style="left:748px;top:1583px;width:284px;height:330px">
    <svg class="roof" style="left:-6px;top:-4px" width="296" height="80" viewBox="0 0 296 80"><polyline points="4,76 148,6 292,76" fill="none" stroke="var(--lime)" stroke-width="10"/></svg>
    <div class="photo house" role="img" aria-label="Worker in safety vest inspecting siding with a clipboard" style="left:0;top:10px;width:284px;height:320px;border-radius:0 0 14px 14px;background:linear-gradient(135deg,#5d7eb3,#8ea6cc 45%,#e66a2a 70%,#d0d5da)"></div>
    <div class="label">MAINTENANCE</div>
  </div>
  <div class="abs svc-card" style="left:1070px;top:1583px;width:284px;height:330px">
    <svg class="roof" style="left:-6px;top:-4px" width="296" height="80" viewBox="0 0 296 80"><polyline points="4,76 148,6 292,76" fill="none" stroke="var(--lime)" stroke-width="10"/></svg>
    <div class="photo house" role="img" aria-label="Roofers installing shingles" style="left:0;top:10px;width:284px;height:320px;border-radius:0 0 14px 14px;background:linear-gradient(135deg,#9fb4c9,#5d5149 50%,#2e2a28)"></div>
    <div class="label">ROOFING</div>
  </div>

  <div class="arrow-btn" style="left:113px;top:2007px;background:#e3e4ea;color:#555">&#8249;</div>
  <div class="arrow-btn" style="left:167px;top:2007px;background:var(--gold);color:#fff">&#8250;</div>
  <div class="abs" style="left:362px;top:2027px;width:478px;height:4px;background:#e4e2de;border-radius:2px"></div>
  <div class="abs" style="left:362px;top:2026px;width:78px;height:6px;background:var(--gold);border-radius:3px"></div>
  <div class="btn" style="left:891px;top:2006px;width:196px;height:48px">VIEW ALL SERVICES</div>
</section>

<!-- PROJECTS -->
<section>
  <div class="abs eyebrow center" style="left:0;top:2166px;width:1200px">PROJECTS</div>
  <h2 class="abs display" style="left:0;top:2196px;width:1200px;text-align:center;font-size:46px">CURRENT PROJECTS</h2>
  <h3 class="abs display" style="left:0;top:2262px;width:1200px;text-align:center;font-size:25px">SEE WHAT WE'RE WORKING ON</h3>
  <p class="abs" style="left:412px;top:2302px;width:376px;text-align:center;font-size:12.5px;line-height:1.6;color:var(--muted)">Check out our latest projects to see how we're turning ideas into reality. From residential renovations to large-scale commercial developments, our portfolio showcases our commitment to quality and detail.</p>

  <svg class="roof" style="left:113px;top:2284px" width="298" height="80" viewBox="0 0 298 80"><polyline points="4,76 149,6 294,76" fill="none" stroke="var(--lime)" stroke-width="10"/></svg>
  <div class="photo house" role="img" aria-label="Workers on ropes cleaning a building facade" style="left:119px;top:2294px;width:286px;height:325px;border-radius:0 0 14px 14px;background:linear-gradient(135deg,#7f8fa5,#425777 50%,#c9a73a 70%,#6e7c8e)"></div>
  <div class="photo" role="img" aria-label="Gardener laying rolls of turf" style="left:124px;top:2634px;width:277px;height:215px;border-radius:12px;background:linear-gradient(180deg,#7c7b66,#6aa13a 55%,#4c7f2b)">
    <div class="abs" style="left:90px;bottom:8px;width:100px;height:5px;background:var(--lime);border-radius:3px"></div>
  </div>

  <div class="photo" role="img" aria-label="Worker in orange hard hat welding" style="left:420px;top:2432px;width:358px;height:417px;border-radius:22px;background:linear-gradient(160deg,#3c3f44 0%,#6b4a2c 40%,#2a2c30 80%)"></div>
  <svg class="roof" style="left:440px;top:2455px" width="318" height="110" viewBox="0 0 318 110"><polyline points="8,20 159,100 310,20" fill="none" stroke="var(--green)" stroke-width="11"/></svg>
  <p class="abs" style="left:450px;top:2700px;width:298px;text-align:center;color:#fff;font-size:12.5px;line-height:1.6">Lorem Ipsum is simply dummy text of the printing and typesetting industry. Lorem Ipsum has been the industry's standard dummy text ever since the 1500s.</p>
  <div class="abs" style="left:522px;top:2807px;color:#fff;font-size:12.5px;font-weight:700;display:flex;gap:12px;align-items:center">VIEW PROJECTS <span style="width:28px;height:28px;border-radius:50%;background:rgba(255,255,255,.3);display:flex;align-items:center;justify-content:center">&#8594;</span></div>

  <svg class="roof" style="left:783px;top:2284px" width="300" height="80" viewBox="0 0 300 80"><polyline points="4,76 150,6 296,76" fill="none" stroke="var(--lime)" stroke-width="10"/></svg>
  <div class="photo house" role="img" aria-label="Worker in safety gear standing on a metal roof" style="left:791px;top:2294px;width:284px;height:325px;border-radius:0 0 14px 14px;background:linear-gradient(180deg,#b8cde3 0%,#8ea7c2 40%,#505a66 70%,#3b434c)"></div>
  <div class="photo" role="img" aria-label="Electrician testing a switchboard with a multimeter" style="left:793px;top:2634px;width:275px;height:215px;border-radius:12px;background:linear-gradient(135deg,#5c6f9c,#d8c04a 45%,#3b4f7c)">
    <div class="abs" style="left:70px;bottom:8px;width:110px;height:5px;background:var(--lime);border-radius:3px"></div>
  </div>
  <div class="btn" style="left:497px;top:2892px;width:204px;height:47px">SEE MORE PROJECTS</div>
</section>

<!-- TESTIMONIALS -->
<section class="testi abs">
  <div class="abs eyebrow center" style="left:0;top:58px;width:1200px">TESTIMONIALS</div>
  <h2 class="abs display" style="left:0;top:88px;width:1200px;text-align:center;font-size:46px">WHAT OUR CLIENTS SAY</h2>
  <h3 class="abs display" style="left:0;top:154px;width:1200px;text-align:center;font-size:25px">HEAR DIRECTLY FROM OUR SATISFIED CUSTOMERS</h3>
  <p class="abs" style="left:320px;top:194px;width:560px;text-align:center;font-size:12.5px;line-height:1.6;color:var(--muted)">Our clients' satisfaction is our top priority. Read what they have to say about their experience working with</p>

  <svg class="roof" style="left:-60px;top:248px" width="320" height="90" viewBox="0 0 320 90"><polyline points="4,86 160,8 316,86" fill="none" stroke="var(--lime)" stroke-width="9"/></svg>
  <div class="photo house" role="img" aria-label="White house with red roof" style="left:-56px;top:258px;width:313px;height:345px;border-radius:0 0 16px 16px;background:linear-gradient(180deg,#c0d4e8 0%,#c8423e 30%,#eceae6 55%,#5c8d3c)"></div>
  <div class="quote-card" style="left:-60px;top:478px;width:266px;height:250px">
    <h4 style="margin-top:30px">PROFESSIONALISM</h4>
    <p style="margin:12px 10px 0 60px;text-align:left">heir meticulous attention to edication to delivering high- a significant impact on our</p>
  </div>

  <svg class="roof" style="left:278px;top:236px" width="644" height="120" viewBox="0 0 644 120"><polyline points="6,116 322,8 638,116" fill="none" stroke="var(--lime)" stroke-width="11"/></svg>
  <div class="photo house" role="img" aria-label="Modern white villa with glass balconies under a blue sky" style="left:286px;top:250px;width:628px;height:358px;border-radius:0 0 20px 20px;background:linear-gradient(180deg,#3f78c6 0%,#8fb4e2 35%,#e9e4dc 55%,#a9785a 75%,#6a8f4c)"></div>
  <svg class="roof" style="left:540px;top:456px" width="120" height="26" viewBox="0 0 120 26"><polyline points="4,4 60,22 116,4" fill="none" stroke="var(--green)" stroke-width="5"/></svg>
  <div class="quote-card" style="left:339px;top:486px;width:522px;height:264px">
    <h4 style="margin-top:30px">EXCEPTIONAL DETAIL AND PROFESSIONALISM</h4>
    <p style="margin:14px 40px 0">"The team surpassed our expectations with their meticulous attention to detail and outstanding professionalism. Their commitment to excellence truly made a difference in the success of our project."</p>
    <div style="margin-top:28px;font-size:12px;font-weight:600">Dalia Fenwick</div>
    <div style="margin-top:6px;font-size:11px;color:var(--muted)">HOUSE OWNER</div>
    <div role="img" aria-label="Client portrait" style="width:36px;height:36px;border-radius:50%;margin:12px auto 0;background:linear-gradient(135deg,#e8c9a6,#b7835c);border:3px solid #f1e3c8"></div>
  </div>

  <svg class="roof" style="left:935px;top:248px" width="320" height="90" viewBox="0 0 320 90"><polyline points="4,86 160,8 316,86" fill="none" stroke="var(--lime)" stroke-width="9"/></svg>
  <div class="photo house" role="img" aria-label="Modern white villa with landscaped front" style="left:942px;top:258px;width:313px;height:345px;border-radius:0 0 16px 16px;background:linear-gradient(180deg,#4d82c8 0%,#9dbde4 35%,#ece7df 55%,#a9785a 75%,#6a8f4c)"></div>
  <div class="quote-card" style="left:993px;top:478px;width:266px;height:250px;text-align:left">
    <h4 style="margin:30px 0 0 98px">REMARKABLE ATTEN</h4>
    <p style="margin:12px 0 0 50px">"The team exceeded our ex detail and unwavering profe quality results truly set ther</p>
  </div>
</section>

<!-- FOOTER BASE -->
<footer class="footer abs">
  <div class="abs brand" style="left:113px;top:88px"><i></i>CALLOWAY</div>
  <p style="left:113px;top:186px;width:260px">Lorem Ipsum is simply dummy text of the printing and typesetting industry. Lorem Ipsum has been the industry's standard dummy text ever since the 1500s</p>
  <h5 style="left:113px;top:296px">CONTACT</h5>
  <div class="line" style="left:113px;top:330px"><svg width="11" height="11" viewBox="0 0 24 24"><path d="M6.6 10.8a15 15 0 006.6 6.6l2.2-2.2c.3-.3.7-.4 1-.2 1.1.4 2.3.6 3.6.6.6 0 1 .4 1 1V20c0 .6-.4 1-1 1C10.6 21 3 13.4 3 4c0-.6.4-1 1-1h3.5c.6 0 1 .4 1 1 0 1.3.2 2.5.6 3.6.1.3 0 .7-.2 1z" fill="var(--gold)"/></svg>(123) 456-7890</div>
  <div class="line" style="left:113px;top:360px"><svg width="11" height="11" viewBox="0 0 24 24"><rect x="2" y="5" width="20" height="14" rx="2" fill="var(--gold)"/><path d="M3 6l9 7 9-7" stroke="var(--footer)" stroke-width="2" fill="none"/></svg>info@calloway.com</div>
  <div class="line" style="left:113px;top:390px;align-items:flex-start;line-height:1.3"><svg width="11" height="13" viewBox="0 0 24 28"><path d="M12 0a9 9 0 00-9 9c0 7 9 19 9 19s9-12 9-19a9 9 0 00-9-9zm0 12a3 3 0 110-6 3 3 0 010 6z" fill="var(--gold)"/></svg><span>718 Larkspur Ave, Fairview, Oregon<br>97024(123) 456-78903</span></div>

  <h5 style="left:448px;top:200px">QUICK LINKS</h5>
  <div class="links">
    <a style="left:448px;top:238px">HOME</a><a style="left:448px;top:268px">ABOUT US</a><a style="left:448px;top:298px">SERVICES</a><a style="left:448px;top:328px">PROJECTS</a><a style="left:448px;top:358px">TESTIMONIALS</a>
    <a style="left:616px;top:238px">NEW ARTICLE</a><a style="left:616px;top:268px">POPULAR ARTICLE</a><a style="left:616px;top:298px">MOST READ</a><a style="left:616px;top:328px">TIPS &amp; TRICKS</a><a style="left:616px;top:358px">FAQ'S</a>
  </div>
  <h5 style="left:616px;top:200px">ARTICLE</h5>
  <h5 style="left:801px;top:200px">SUBSCRIBE TO OUR NEWSLETTER</h5>
  <div class="field" style="left:801px;top:236px;width:286px;height:38px;border-radius:10px;font-size:11px">EMAIL</div>
  <div class="btn" style="left:988px;top:236px;width:99px;height:38px;border-radius:10px;font-size:10px;box-shadow:none">SUBSCRIBE</div>
  <h5 style="left:801px;top:366px">SOCIAL MEDIA</h5>
  <div class="abs" style="left:803px;top:402px;display:flex;gap:22px">
    <i style="width:14px;height:14px;border-radius:50%;background:var(--gold);display:block"></i>
    <i style="width:14px;height:14px;border-radius:50%;background:var(--gold);display:block"></i>
    <i style="width:14px;height:14px;border-radius:3px;background:var(--gold);display:block"></i>
  </div>
  <div class="abs" style="left:113px;top:448px;width:974px;height:1px;background:#555c5c"></div>
  <div class="abs" style="left:0;top:464px;width:1200px;text-align:center;font-size:11px;color:#b9bcbc">©Copyright Calloway Building &amp; Landscaping 2024. All Right Reserved</div>
</footer>

<!-- CONTACT -->
<section>
  <div class="abs" style="left:113px;top:3862px;width:974px;height:518px;background:var(--panel);border-radius:26px"></div>
  <svg class="roof" style="left:150px;top:3896px" width="402" height="110" viewBox="0 0 402 110"><polyline points="5,105 201,8 397,105" fill="none" stroke="var(--lime)" stroke-width="11"/></svg>
  <div class="photo house" role="img" aria-label="Modern white house against a cloudy sky" style="left:154px;top:3906px;width:394px;height:427px;border-radius:0 0 20px 20px;background:linear-gradient(180deg,#5a6c86 0%,#303f58 50%,#1b2336)"></div>
  <div class="abs eyebrow center" style="left:154px;top:4043px;width:394px">CONTACT US</div>
  <h2 class="abs display" style="left:154px;top:4070px;width:394px;text-align:center;color:#fff;font-size:46px">GET IN TOUCH</h2>
  <h3 class="abs display" style="left:154px;top:4134px;width:394px;text-align:center;color:#fff;font-size:25px">WE'RE HERE TO HELP</h3>
  <p class="abs" style="left:178px;top:4174px;width:346px;text-align:center;color:#fff;font-size:12.5px;line-height:1.55">Have questions or need a quote? Reach out to us, and we'll be happy to assist you with your project needs. Our team is ready to provide the information and support you need.</p>

  <div class="abs" style="left:590px;top:3909px;width:469px;height:424px;background:var(--field);border-radius:20px"></div>
  <div class="field" style="left:603px;top:3964px;width:209px;height:43px">First Name</div>
  <div class="field" style="left:831px;top:3964px;width:209px;height:43px">Last Name</div>
  <div class="field" style="left:603px;top:4024px;width:209px;height:43px">Email</div>
  <div class="field" style="left:831px;top:4024px;width:209px;height:43px">Phone Number</div>
  <div class="field" style="left:603px;top:4085px;width:437px;height:43px;justify-content:space-between">Select Services<svg width="12" height="8" viewBox="0 0 12 8"><path d="M1 1l5 5 5-5" stroke="#999" stroke-width="1.6" fill="none"/></svg></div>
  <div class="field" style="left:603px;top:4145px;width:437px;height:92px;align-items:flex-start;padding-top:14px">Message</div>
  <div class="btn" style="left:603px;top:4256px;width:437px;height:45px;box-shadow:none">SUMBIT</div>
</section>

</body>
</html>
```